HIgh-end jewelry designer needs a business card design

I need a business card design for the ecclectic & rather expensive jewelry designs. My approach to my work is to combine very old jewelry offset with contemporary items. I enjoy the idea of legacy as well as repurposing finely crafted items that are not possible to create any longer. My desire is to celebrate the past in a contemporary & funky way. The name of my business is VELLORINE. I see my business card design as simple & yet enigmatic as possible. In the end... clean, simple & understated is the look I am after. Thank you for your consideration...

Target Market(s)

I will use this business card for the trade as well as customers

Industry/Entity Type

Business

Contact Information for Business Card

Marta Quorrin Owner/Designer 555-203-7718

Requirements
Must have
• Clean & simple sophisticated design using the word "Vellorinne" as the logo. I like the idea of a play on the word itself, perhaps even using different fonts (i.e.: a bold helvetica combined with a lovely script). I'm afraid to say more because I don't want to limit creative input. Gosh, sometimes it's ok to break the rules!
Nice to have
• In my mind, I have imagined this business card to be simple, using my company name "Vellorine" in a playful yet sophisticated manner. I believe that doing something beautifully simple can be a true challenge. I have imagined something with just black & white, however I am open to ideas... after all that's why I'm here!
Should not have
• As Mozart once said... "It has too many notes!" I know I'm being silly, but I don't want it to be complicated or overly ornate.

```html
<!DOCTYPE html>
<html lang="en">
<head>
<meta charset="utf-8">
<title>Vellorine – Business Card</title>
<link href="https://fonts.googleapis.com/css2?family=Great+Vibes&family=Lora:wght@400;500&family=Cormorant+Garamond:wght@500;600&display=swap" rel="stylesheet">
<style>
  :root {
    --backdrop: #4a0507;
    --gold: #f1a620;
    --gold-deep: #e4930f;
    --wine: #8c1b1f;
    --ink: #5b1a10;
    --photo-dark: #2a1408;
    --photo-mid: #6b3a12;
    --photo-glow: #f4c25a;
  }
  * { margin: 0; padding: 0; box-sizing: border-box; }
  html, body {
    width: 1200px;
    height: 900px;
    overflow: hidden;
    background: var(--backdrop);
  }
  .card {
    position: absolute;
    left: 75px;
    top: 150px;
    width: 1050px;
    height: 600px;
    display: flex;
    overflow: hidden;
    box-shadow: 0 20px 50px rgba(0, 0, 0, 0.45);
  }
  .band {
    position: relative;
    height: 100%;
    background: linear-gradient(160deg, var(--gold) 0%, var(--gold-deep) 100%);
  }
  .band--identity { width: 330px; }
  .band--contact { width: 160px; }
  .hero-photo {
    width: 560px;
    height: 100%;
    background:
      radial-gradient(circle at 42% 68%, var(--photo-glow) 0%, rgba(244, 194, 90, 0.5) 12%, rgba(107, 58, 18, 0) 34%),
      radial-gradient(ellipse at 70% 35%, #c98c5a 0%, rgba(201, 140, 90, 0) 40%),
      linear-gradient(90deg, var(--photo-dark) 0%, var(--photo-mid) 60%, #8a5a2c 100%);
  }
  .identity {
    position: absolute;
    width: 600px;
    height: 330px;
    left: -135px;
    top: 135px;
    transform: rotate(-90deg);
    padding: 18px 0 0 70px;
  }
  .brand-name {
    font-family: "Great Vibes", cursive;
    font-size: 150px;
    line-height: 1;
    color: var(--wine);
  }
  .owner-name {
    margin-top: 6px;
    font-family: "Cormorant Garamond", serif;
    font-weight: 600;
    font-size: 46px;
    line-height: 1;
    color: var(--ink);
    padding-left: 150px;
  }
  .owner-title {
    margin-top: 4px;
    font-family: "Cormorant Garamond", serif;
    font-weight: 500;
    font-size: 30px;
    color: var(--ink);
    padding-left: 150px;
  }
  .phone {
    position: absolute;
    width: 600px;
    height: 160px;
    left: -220px;
    top: 220px;
    transform: rotate(-90deg);
    display: flex;
    align-items: center;
    justify-content: center;
    font-family: "Lora", serif;
    font-weight: 500;
    font-size: 44px;
    letter-spacing: 1px;
    color: var(--wine);
  }
</style>
</head>
<body>
  <div class="card">
    <div class="band band--identity">
      <div class="identity">
        <div class="brand-name">Vellorine</div>
        <div class="owner-name">Marta Quorrin</div>
        <div class="owner-title">Owner/Designer</div>
      </div>
    </div>
    <div class="hero-photo" role="img" aria-label="Photograph of a woman with ornate metal wire hair pieces holding a glowing golden light in her cupped hands against a dark background"></div>
    <div class="band band--contact">
      <div class="phone">555-203-7718</div>
    </div>
  </div>
</body>
</html>
```